BLUE HAVEN (Business Card for Training Company)

Blue Haven is a training and consultancy company with a focus on executive protection and medical. I would like the card to be nice and sharp, not overdone and in black and red. I would also like it to highlight that it is "A Dravin Company"

I would like it to be simple and highlight a few things.

1. Name
2. Title
3. Phone Number
4. Email

I would also like www.dravinholdings.example/blue-haven to be on the card somewhere.

Target Market(s)

Security Companies

Industry/Entity Type

Security

Contact Information for Business Card

Blue Haven is a training and consultancy company with a focus on executive protection and medical. I would like the card to be nice and sharp, not overdone and in black and red. I would also like it to highlight that it is "A Dravin Company" I would like it to be simple and highlight a few things. 1. Name 2. Title 3. Phone Number 4. Email I would also like www.dravinholdings.example/blue-haven to be on the card somewhere.

Requirements
Must have
• A Dravin Company listed on the card and the website
Nice to have
• Highlight Medical Training, Consultancy & Executive Protection Courses

```html
<!DOCTYPE html>
<html lang="en">
<head>
<meta charset="utf-8">
<title>Blue Haven — Business Card</title>
<link href="https://fonts.googleapis.com/css2?family=Michroma&display=swap" rel="stylesheet">
<style>
  :root {
    --backdrop: #9c9c9c;
    --paper-light: #f8f8f8;
    --paper-dark: #d9d9d9;
    --maroon: #5c0003;
    --maroon-deep: #470004;
    --maroon-darker: #3d0003;
    --ink: #0c0c0c;
    --white: #f4f4f4;
    --white-soft: #e2c9ca;
  }
  * { box-sizing: border-box; margin: 0; padding: 0; }
  html, body {
    width: 1200px; height: 1200px; overflow: hidden;
    background: var(--backdrop);
    font-family: "Michroma", sans-serif;
  }
  .canvas { position: relative; width: 1200px; height: 1200px; }
  .card {
    position: absolute; left: 250px; width: 700px; height: 420px;
    overflow: hidden;
  }
  .card-front {
    top: 150px;
    background: radial-gradient(ellipse at 75% 95%, var(--paper-light) 0%, #ececec 45%, var(--paper-dark) 100%);
  }
  .card-back {
    top: 630px;
    background: linear-gradient(200deg, var(--maroon-deep) 0%, #4a0005 50%, var(--maroon-darker) 100%);
  }
  .brackets { position: absolute; inset: 0; width: 700px; height: 420px; }
  .wordmark {
    position: absolute; font-size: 46px; line-height: 58px; letter-spacing: 1px;
  }
  .card-front .wordmark { left: 145px; top: 62px; color: var(--maroon); }
  .card-back .wordmark { left: 241px; top: 152px; color: var(--white); }
  .person-name {
    position: absolute; left: 148px; top: 230px;
    font-size: 20px; font-weight: 400; letter-spacing: 2px; color: var(--ink);
    white-space: nowrap;
  }
  .person-title {
    position: absolute; left: 149px; top: 260px;
    font-size: 12px; letter-spacing: 3px; color: var(--ink);
    white-space: nowrap;
  }
  .contact-list { position: absolute; left: 146px; top: 306px; list-style: none; }
  .contact-item {
    display: flex; align-items: flex-start; gap: 12px;
    font-size: 9px; letter-spacing: 1.2px; line-height: 12px; color: var(--ink);
    margin-bottom: 12px; white-space: nowrap;
  }
  .contact-item svg { width: 14px; height: 14px; flex: none; fill: var(--maroon); }
  .at { color: var(--maroon); }
  .parent-line {
    position: absolute; left: 243px; top: 298px;
    font-size: 10px; letter-spacing: 3px; color: var(--white);
    white-space: nowrap;
  }
  .website {
    position: absolute; left: 243px; top: 318px;
    font-size: 8px; letter-spacing: 1px; color: var(--white-soft);
    white-space: nowrap;
  }
</style>
</head>
<body>
<div class="canvas">

  <section class="card card-front">
    <svg class="brackets" viewBox="0 0 700 420" aria-hidden="true">
      <polygon fill="var(--maroon)" points="63,0 97,0 97,231 0,290 0,249 63,212"/>
      <polygon fill="var(--maroon)" points="700,134 610,134 610,406 633,420 700,420 646,386 646,169 700,169"/>
    </svg>
    <div class="wordmark">BLUE<br>HAVEN</div>
    <h1 class="person-name">NAME NAME NAME</h1>
    <p class="person-title">THE TITTLE THE TITTLE</p>
    <ul class="contact-list">
      <li class="contact-item">
        <svg viewBox="0 0 24 24"><path d="M12 2a7 7 0 0 0-7 7c0 5 7 13 7 13s7-8 7-13a7 7 0 0 0-7-7zm0 9.5A2.5 2.5 0 1 1 12 6.5a2.5 2.5 0 0 1 0 5z"/></svg>
        <span>LOCATION LOCATION LOCATION<br>LOCATION LOCATION LOCATION</span>
      </li>
      <li class="contact-item">
        <svg viewBox="0 0 24 24"><path d="M6.6 10.8a15 15 0 0 0 6.6 6.6l2.2-2.2a1 1 0 0 1 1-.25 11.4 11.4 0 0 0 3.6.57 1 1 0 0 1 1 1V20a1 1 0 0 1-1 1A17 17 0 0 1 3 4a1 1 0 0 1 1-1h3.5a1 1 0 0 1 1 1c0 1.25.2 2.45.57 3.57a1 1 0 0 1-.25 1z"/></svg>
        <span>+00 0000 1234 56789</span>
      </li>
      <li class="contact-item">
        <svg viewBox="0 0 24 24"><path d="M2 5h20v3l-10 6L2 8z M2 10l10 6 10-6v9H2z"/></svg>
        <span>INFO<span class="at">@</span>DRAVINHOLDINGS.EXAMPLE</span>
      </li>
    </ul>
  </section>

  <section class="card card-back">
    <svg class="brackets" viewBox="0 0 700 420" aria-hidden="true">
      <rect x="0" y="0" width="63" height="240" fill="var(--maroon-darker)" opacity="0.5"/>
      <polygon fill="var(--maroon)" points="63,0 97,0 97,231 0,290 0,249 63,212"/>
      <polygon fill="var(--maroon-darker)" points="646,169 700,169 700,420 646,386"/>
      <polygon fill="var(--maroon)" points="700,134 610,134 610,406 633,420 700,420 646,386 646,169 700,169"/>
    </svg>
    <div class="wordmark">BLUE<br>HAVEN</div>
    <p class="parent-line">A DRAVIN COMPANY</p>
    <p class="website">WWW.DRAVINHOLDINGS.EXAMPLE/BLUE-HAVEN</p>
  </section>

</div>
</body>
</html>
```